Real Estate Listing Signs for standard Yard arms

I need real estate listing signs done, for the standard sized sign to be hung beneath a white yard arm. To match existing logo. Information to be included:
-Logo
-Business name
-Phone number
-Marden Fosk Tundra Circle & Marden Fosk realty logos (smaller print)

Colors to be Red and anywhere in the gray scale between black and white, or a combination of those.

Target Market(s)

Drive by visuals

Industry/Entity Type

Real Estate Agent

Colors

Designer to choose only greyscale colors for use in the design.

Requirements
Must have
• My Logo and business name in same/similar font to whats provided, the MF tundra circle logo (small on bottom or corner somewhere), My phone number, and a decent amount of red coloration on the sign.

```html
<!DOCTYPE html>
<html lang="en">
<head>
<meta charset="utf-8">
<title>Velmar Realty – Yard Sign</title>
<link rel="stylesheet" href="https://fonts.googleapis.com/css2?family=Montserrat:wght@500;700;800&display=swap">
<style>
  :root {
    --sign-red: #ee2424;
    --sign-charcoal: #333132;
    --sign-white: #ffffff;
    --page-bg: #ececec;
  }
  html, body {
    margin: 0;
    padding: 0;
    width: 728px;
    height: 1200px;
    overflow: hidden;
    background: var(--page-bg);
  }
  .canvas {
    position: relative;
    width: 728px;
    height: 1200px;
  }
  .yard-sign {
    position: absolute;
    left: 24px;
    top: 345px;
    width: 680px;
    height: 510px;
    display: block;
    box-shadow: 0 10px 24px rgba(0,0,0,0.18);
  }
  .sign-text {
    font-family: "Montserrat", sans-serif;
  }
  .brand-mark-name { font-weight: 800; fill: var(--sign-charcoal); }
  .business-name { font-weight: 800; fill: var(--sign-charcoal); }
  .agent-name { font-weight: 700; fill: var(--sign-white); }
  .contact-line { font-weight: 700; fill: var(--sign-white); }
  .brokerage-name { font-weight: 700; fill: var(--sign-charcoal); }
  .disclaimer { font-weight: 700; fill: var(--sign-charcoal); font-variant: small-caps; }
</style>
</head>
<body>
<main class="canvas">
  <svg class="yard-sign" viewBox="0 0 1180 885" xmlns="http://www.w3.org/2000/svg" aria-label="Velmar Realty listing sign">
    <!-- background bands -->
    <rect class="sign-base" x="0" y="0" width="1180" height="885" fill="var(--sign-white)"/>
    <rect class="red-band" x="0" y="200" width="1180" height="560" fill="var(--sign-red)"/>
    <path class="charcoal-swoosh" d="M0,0 H1180 V320 Q590,700 0,240 Z" fill="var(--sign-charcoal)"/>
    <path class="white-crest" d="M0,0 H1180 V240 Q590,620 0,240 Z" fill="var(--sign-white)"/>

    <!-- brand mark -->
    <g class="brand-mark">
      <rect x="390" y="105" width="85" height="85" fill="var(--sign-red)"/>
      <text class="sign-text brand-mark-name" x="495" y="177" font-size="76">VELMAR</text>
    </g>

    <!-- business name -->
    <text class="sign-text business-name" x="590" y="340" font-size="62" text-anchor="middle" letter-spacing="2">VELMAR REALTY</text>

    <!-- agent name -->
    <text class="sign-text agent-name" x="590" y="610" font-size="104" text-anchor="middle" textLength="1000" lengthAdjust="spacingAndGlyphs">DANA VELMAR</text>

    <!-- contact line -->
    <g class="contact-line-group">
      <path class="phone-icon" fill="var(--sign-white)"
        d="M85,660 l12,-6 l12,20 l-9,6 q4,12 16,20 l7,-8 l19,13 l-6,12 q-30,6 -51,-57 Z"/>
      <text class="sign-text contact-line" x="135" y="698" font-size="48" textLength="340" lengthAdjust="spacingAndGlyphs">907-555-0148</text>
      <line class="contact-divider" x1="498" y1="650" x2="498" y2="705" stroke="var(--sign-white)" stroke-width="3"/>
      <g class="email-icon" fill="none" stroke="var(--sign-white)" stroke-width="4">
        <rect x="522" y="662" width="42" height="30"/>
        <polyline points="522,662 543,680 564,662"/>
        <line x1="522" y1="692" x2="538" y2="676"/>
        <line x1="564" y1="692" x2="548" y2="676"/>
      </g>
      <text class="sign-text contact-line" x="580" y="696" font-size="40" textLength="522" lengthAdjust="spacingAndGlyphs">DVELMAR@MAIL.COM</text>
    </g>

    <!-- brokerage footer -->
    <g class="brokerage">
      <text class="sign-text brokerage-name" x="75" y="826" font-size="40">MF TUNDRA CIRCLE</text>
      <text class="sign-text brokerage-name" x="75" y="857" font-size="20" letter-spacing="1">MARDEN FOSK REALTY</text>
    </g>
    <text class="sign-text disclaimer" x="675" y="812" font-size="28">Each office independently</text>
    <text class="sign-text disclaimer" x="675" y="842" font-size="28">owned and Operated</text>
  </svg>
</main>
</body>
</html>
```